card design for engineering consultancy

engineering drafting and project management company the provides drafting services for.
Electrical, Hydraulic, Mechanical, and Civil services
The company is called Q7R Services and logo is as attached
Information on card should be.
1. Logo
2.website : Q7RServices.example
3. email : info@Q7RServices.example
4. Phone: (+61) 400512836
5. Motto: Design - Document - Develop - Deliver

this card should be basically used for business identification only

Target Market(s)

electricians plumbers air conditioning installers and civil contractors

Industry/Entity Type

engineering, drafting, electrical, plumbing, airconditioning, civil

Contact Information for Business Card

1. Logo 2.website : Q7RServices.example 3. email : info@Q7RServices.example 4. Phone: (+61) 400512836 5. Motto: Design - Document - Develop - Deliver

Font styles to use
Serif

Requirements
Must have
• logo
Nice to have
• something inovative and different that makes it stand out from being just another business card

```html
<!DOCTYPE html>
<html lang="en">
<head>
<meta charset="utf-8">
<title>Q7R Services – Business Card</title>
<link href="https://fonts.googleapis.com/css2?family=Montserrat:wght@400;600;700&family=Oswald:wght@500&display=swap" rel="stylesheet">
<style>
  :root {
    --backdrop: #e7e4df;
    --card-white: #ffffff;
    --card-dark: #222222;
    --brand-red: #d2343f;
    --brand-grey: #555555;
    --ink: #333333;
    --faint-grey: #e2e2e2;
    --rule: #444444;
    --light: #ffffff;
    --back-mark: #8a8a8a;
  }
  * { box-sizing: border-box; margin: 0; padding: 0; }
  html, body { width: 1125px; height: 1200px; overflow: hidden; }
  body { background: var(--backdrop); font-family: "Montserrat", sans-serif; position: relative; }

  .card { position: absolute; overflow: hidden; box-shadow: 0 4px 12px rgba(0,0,0,.18); }

  /* Front */
  .card--front { left: 150px; top: 93px; width: 836px; height: 490px; background: var(--card-white); }
  .brand-watermark { position: absolute; right: 20px; top: 38px; font-weight: 700; font-size: 60px; color: var(--faint-grey); letter-spacing: 2px; line-height: 1; white-space: nowrap; }
  .brand-lockup { position: absolute; left: 30px; top: 148px; display: flex; align-items: center; gap: 14px; white-space: nowrap; }
  .brand-lockup__square { width: 30px; height: 30px; background: var(--brand-red); }
  .brand-lockup__name { font-weight: 700; font-size: 40px; color: var(--brand-grey); letter-spacing: 2px; line-height: 1; }

  .person { position: absolute; left: 30px; top: 240px; }
  .person__name { font-weight: 700; font-size: 38px; color: var(--brand-red); letter-spacing: -0.5px; line-height: 1.1; }
  .person__role { font-size: 21px; color: var(--ink); margin-top: 4px; }
  .divider { position: absolute; left: 30px; right: 30px; top: 327px; height: 2px; background: var(--rule); }

  .contact-list { position: absolute; left: 32px; top: 340px; list-style: none; }
  .contact-list li { display: flex; align-items: center; gap: 18px; font-size: 22px; color: var(--ink); height: 34px; white-space: nowrap; }
  .contact-list svg { width: 20px; height: 20px; fill: var(--brand-red); flex: none; }

  .address { position: absolute; right: 40px; top: 370px; font-size: 22px; color: var(--ink); line-height: 33px; font-style: normal; }

  .motto-band { position: absolute; left: 0; bottom: 0; width: 836px; height: 38px; }
  .motto { position: absolute; right: 28px; bottom: 7px; font-family: "Oswald", sans-serif; font-weight: 500; font-size: 18px; line-height: 1.2; color: var(--light); white-space: nowrap; }

  /* Back */
  .card--back { left: 150px; top: 614px; width: 872px; height: 496px; background: var(--card-dark); }
  .back-lockup { position: absolute; left: 0; right: 0; top: 180px; display: flex; justify-content: center; align-items: center; gap: 20px; white-space: nowrap; }
  .back-lockup__square { width: 44px; height: 44px; background: var(--back-mark); }
  .back-lockup__name { font-weight: 700; font-size: 64px; color: var(--back-mark); letter-spacing: 3px; }
  .services { position: absolute; left: 0; right: 0; top: 402px; text-align: center; font-family: "Oswald", sans-serif; font-weight: 500; font-size: 30px; line-height: 1.2; color: var(--light); white-space: nowrap; }
</style>
</head>
<body>

<section class="card card--front" aria-label="Business card front">
  <div class="brand-watermark" aria-hidden="true">Q7R Services</div>
  <div class="brand-lockup">
    <span class="brand-lockup__square"></span>
    <span class="brand-lockup__name">Q7R Services</span>
  </div>

  <div class="person">
    <h1 class="person__name">DANIEL HARTLEY</h1>
    <p class="person__role">Managing Director</p>
  </div>
  <div class="divider"></div>

  <ul class="contact-list">
    <li>
      <svg viewBox="0 0 24 24" aria-hidden="true"><path d="M6.6 10.8a15.1 15.1 0 0 0 6.6 6.6l2.2-2.2a1 1 0 0 1 1-.25 11.4 11.4 0 0 0 3.6.57 1 1 0 0 1 1 1V20a1 1 0 0 1-1 1A17 17 0 0 1 3 4a1 1 0 0 1 1-1h3.5a1 1 0 0 1 1 1c0 1.25.2 2.45.57 3.57a1 1 0 0 1-.25 1z"/></svg>
      (+61) 400512836
    </li>
    <li>
      <svg viewBox="0 0 24 24" aria-hidden="true"><path d="M2 5h20v1.6l-10 7.2L2 6.6z M2 9l10 7 10-7v10H2z"/></svg>
      info@Q7RServices.example
    </li>
    <li>
      <svg viewBox="0 0 24 24" aria-hidden="true"><circle cx="12" cy="12" r="10"/><path d="M2 12h20M12 2c3 3 3 17 0 20M12 2c-3 3-3 17 0 20" fill="none" stroke="#fff" stroke-width="1.4"/></svg>
      www.Q7RServices.example
    </li>
  </ul>

  <address class="address">421, Address line here<br>Country Name, 45452</address>

  <svg class="motto-band" viewBox="0 0 836 38" aria-hidden="true">
    <polygon points="0,12 475,12 462,25 0,25" fill="#d2343f"/>
    <polygon points="490,0 836,0 836,38 452,38" fill="#555555"/>
  </svg>
  <p class="motto">DESIGN - DOCUMENT - DEVELOP - DELIVER</p>
</section>

<section class="card card--back" aria-label="Business card back">
  <div class="back-lockup">
    <span class="back-lockup__square"></span>
    <span class="back-lockup__name">Q7R Services</span>
  </div>
  <p class="services">ELECTRICAL &nbsp;|&nbsp; HYDRAULIC &nbsp;|&nbsp; MECHANICAL AND CIVIL SERVICES</p>
</section>

</body>
</html>
```